Veteran owned/staffed Organization that hires Veterans into Ironworking

Please see attached documents for all details and info.
We want a tri-fold brochure to use as a recruiting tool.
Our slogan is:
"Revolutionizing the skilled workforce, one Veteran at a time"
Veteran Apprenticeship Program in Ironworking
Skills/Traits: Welding, bolting, rigging, connecting
Teamwork, camaraderie, TK Grant, Skilled Labor, Career, Community service
OJT, Apprenticeship, Career
Due to the large number of retirees from the baby boomer generation, ironworkers are in high demand. In Texas, the construction industry is on the rise and due to our training regiment, an average of 40 hrs/wk are worked. Our apprenticeship program follows the PLWTO curriculum and at the end of the 3-year course involving classroom learning, OJT and practical application the apprentice achieves journeymen status in ironworking. Journeyman status opens the door to possible postions like foremen, crane operators and project managers. Ironworkers perform their duties on steel structures that provide a skeleton for commercial buildings like hospitals, schools and skyscrapers. Some of the key skilled trades of ironworking are welding, rigging, bolting and connecting.
All Things Veterans
Camaraderie and Culture
-Veteran owned and majority staffed organization who are committed to the mission of providing opportunitites to Veterans
-Graduation celebration after completion of initial training period, holiday parties and get togethers at HQBs
-Work with other Veterans and always have your teammate’s six
-We’re building America, one Veteran career at a time
Professional Support
BDR is committed to providing Veterans with supportive services designed to assist you and your families in the following areas:
Financial, family and work-related support.
Community Service
Disaster Response
Louisiana Flooding - Sept 2016
As the 15th anniversery of 9/11 approached BDR worked to find a volunteer opportunity. An ambitious plan was formed to respond to the devastating 1000-year flood event in Baton Rouge. With little time for planning, BDR organized all the tools and supplies necessary to take 24 Veterans to assist a community in extreme poverty. The team gutted the homes of nine residents which included: single mothers, handicapped elderaly and a Korean War Veterans
Hurricane Orlend - Oct 2016
In a period of 24 hours BDR mobilized 16 Veterans with the supplies neccessary to be 100% self-reliant. The team arrived in Holly Hill, SC 8 hours after Hurrican Orlend made landfall. During a period of 2 days, BDR provided over 5,000 meals, distributed 40,000 bottles of water and removed nearly 100 trees.

Target Market(s)

Veterans who are interested in becoming Ironworkers. Usually under the age of 40, have served in the military and are in the Texas area.

Industry/Entity Type

Construction

Font styles to use
Other font styles liked:
• Microgramma in some places (Logo font) and Serif type font for the bulk

Requirements
Must have
• The colors and logo mentioned in the template guidelines document.
• The slogan
• "Revolutionizing the skilled workforce, one Veteran at a time"
Nice to have
• Some charts and graphs if possible?

```html
<!DOCTYPE html>
<html lang="en">
<head>
<meta charset="utf-8">
<title>BDR Tri-Fold Brochure – Inside Spread</title>
<link rel="stylesheet" href="https://fonts.googleapis.com/css2?family=Michroma&family=Tinos:wght@400;700&display=swap">
<style>
:root{
  --navy:#14243b;
  --navy-deep:#0d192b;
  --paper:#f3f4f6;
  --paper-shade:#e3e5e9;
  --ink:#1b1b1f;
  --white:#ffffff;
  --stage:#e4e4e6;
  --sky-top:#4f8fd8;
  --sky-low:#a9c9ee;
  --steel:#3a2a2a;
}
*{box-sizing:border-box;margin:0;padding:0}
html,body{width:971px;height:1200px;overflow:hidden;background:var(--stage)}
.spread{position:absolute;left:0;top:225px;width:971px;height:750px;overflow:hidden;box-shadow:0 4px 14px rgba(0,0,0,.25)}
.spread-art{position:absolute;inset:0}
.panel{position:absolute;top:0;height:750px;width:323px}
.panel--career{left:0}
.panel--veterans{left:324px}
.panel--service{left:648px}
.panel-title{position:absolute;font-family:"Michroma",sans-serif;font-size:17px;line-height:23px;text-align:center;letter-spacing:-.2px;border-radius:3px;text-transform:uppercase;white-space:nowrap}
.panel-title--dark{background:var(--navy);color:var(--white);box-shadow:0 0 0 2px var(--paper),0 0 0 3px #9aa3af}
.panel-title--light{background:var(--white);color:var(--navy);box-shadow:0 0 0 2px var(--navy),0 0 0 3px #8b96a6}
.panel--career .panel-title{left:27px;top:234px;width:269px;height:56px;padding-top:5px}
.panel--veterans .panel-title{left:19px;top:235px;width:279px;height:33px;padding-top:5px}
.panel--service .panel-title{left:15px;top:235px;width:278px;height:33px;padding-top:5px}
.subhead{position:absolute;left:0;width:323px;top:281px;text-align:center;font-family:"Tinos",serif;font-weight:700;font-size:18px;text-decoration:underline;text-underline-offset:3px}
.panel--veterans .subhead{color:var(--white)}
.panel--service .subhead{color:var(--ink)}
.body-copy{font-family:"Tinos",serif;font-size:12.6px;line-height:14.8px;text-align:justify;color:var(--ink)}
.panel--career .body-copy{position:absolute;left:16px;top:323px;width:292px}
.checklist{position:absolute;list-style:none;font-family:"Tinos",serif;font-size:12.6px;line-height:14.3px}
.checklist li{position:relative;padding-left:25px}
.check{position:absolute;left:4px;top:2px;width:12px;height:12px}
.checklist--veterans{left:16px;top:326px;width:296px;color:var(--white)}
.checklist--veterans li{margin-bottom:17px}
.checklist--veterans li:nth-child(2){margin-bottom:19px}
.checklist--service{left:16px;top:326px;width:296px;color:var(--ink)}
.checklist--service li{margin-bottom:14px}
.event-title{font-size:13.2px}
.event-title b{font-weight:700}
.checklist--service .body-copy{margin-top:6px;font-size:11.4px;line-height:13.1px}
.web-address{position:absolute;bottom:6px;left:0;width:323px;display:flex;align-items:center;justify-content:center;gap:8px;font-family:"Michroma",sans-serif;font-size:11px;color:var(--white)}
.web-address::before,.web-address::after{content:"";width:20px;height:1px;background:var(--white)}
</style>
</head>
<body>
<main class="spread">
  <svg class="spread-art" width="971" height="750" viewBox="0 0 971 750">
    <defs>
      <linearGradient id="sky" x1="0" y1="0" x2="0" y2="1">
        <stop offset="0" stop-color="var(--sky-top)"/><stop offset="1" stop-color="var(--sky-low)"/>
      </linearGradient>
      <linearGradient id="paper" x1="0" y1="0" x2="1" y2="0">
        <stop offset="0" stop-color="var(--paper)"/><stop offset="1" stop-color="var(--paper-shade)"/>
      </linearGradient>
      <linearGradient id="crane" x1="0" y1="0" x2="1" y2="1">
        <stop offset="0" stop-color="#6c6a74"/><stop offset=".45" stop-color="#c4472a"/><stop offset="1" stop-color="#50505a"/>
      </linearGradient>
      <linearGradient id="helmet" x1="0" y1="0" x2="1" y2="0">
        <stop offset="0" stop-color="#9a9a9a"/><stop offset=".55" stop-color="#c8c8c8"/><stop offset="1" stop-color="#2f8a4a"/>
      </linearGradient>
      <linearGradient id="crew" x1="0" y1="0" x2="0" y2="1">
        <stop offset="0" stop-color="#7d8c5a"/><stop offset=".6" stop-color="#4d4f58"/><stop offset="1" stop-color="#8a8f78"/>
      </linearGradient>
    </defs>
    <rect role="img" aria-label="Photo: ironworkers guiding a red crane hook over steel beams" x="0" y="0" width="324" height="200" fill="url(#crane)"/>
    <rect role="img" aria-label="Photo: veteran ironworker in a green hard hat on a steel frame site" x="324" y="0" width="324" height="210" fill="url(#helmet)"/>
    <rect role="img" aria-label="Photo: veteran team joining hands in a circle outdoors" x="648" y="0" width="323" height="200" fill="url(#crew)"/>
    <rect role="img" aria-label="Photo: steel building skeleton against a blue sky with workers on the beams" x="0" y="540" width="971" height="210" fill="url(#sky)"/>
    <polygon fill="var(--navy)" points="0,128 323,168 648,188 971,128 971,640 648,580 323,566 0,640"/>
    <polygon fill="var(--navy-deep)" points="323,168 648,188 648,196 323,176"/>
    <polygon fill="url(#paper)" points="0,142 323,180 323,556 0,628"/>
    <polygon fill="url(#paper)" points="648,200 971,142 971,628 648,570"/>
  </svg>

  <section class="panel panel--career">
    <h2 class="panel-title panel-title--dark">OJT, Apprenticeship,<br>Career</h2>
    <p class="body-copy">Due to the large number of retirees from the baby boomer generation, ironworkers are in high demand. In Texas, the construction industry is on the rise and due to our training regiment, an average of 40 hrs/wk are worked. Our apprenticeship program follows the PLWTO curriculum and at the end of the 3-year course involving classroom learning, OJT and practical application the apprentice achieves journeymen status in ironworking. Journeyman status opens the door to possible postions like foremen, crane operators and project managers. Ironworkers perform their duties on steel structures that provide a skeleton for commercial buildings like hospitals, schools and skyscrapers. Some of the key skilled trades of ironworking are welding, rigging, bolting and connecting.</p>
    <p class="web-address">www.bdrtexas.com</p>
  </section>

  <section class="panel panel--veterans">
    <h2 class="panel-title panel-title--light">All Things Veterans</h2>
    <h3 class="subhead">Camaraderie and Culture</h3>
    <ul class="checklist checklist--veterans">
      <li><svg class="check" viewBox="0 0 12 12"><rect x=".5" y=".5" width="11" height="11" fill="none" stroke="currentColor"/><path d="M2.5 6l2.5 2.5 5-6" fill="none" stroke="currentColor" stroke-width="1.6"/></svg>Veteran owned and majority staffed organization who are committed to the mission of providing opportunitites to Veterans</li>
      <li><svg class="check" viewBox="0 0 12 12"><rect x=".5" y=".5" width="11" height="11" fill="none" stroke="currentColor"/><path d="M2.5 6l2.5 2.5 5-6" fill="none" stroke="currentColor" stroke-width="1.6"/></svg>Graduation celebration after completion of initial training period, holiday parties and get togethers at HQBs</li>
      <li><svg class="check" viewBox="0 0 12 12"><rect x=".5" y=".5" width="11" height="11" fill="none" stroke="currentColor"/><path d="M2.5 6l2.5 2.5 5-6" fill="none" stroke="currentColor" stroke-width="1.6"/></svg>Work with other Veterans and always have your teammate’s six</li>
      <li><svg class="check" viewBox="0 0 12 12"><rect x=".5" y=".5" width="11" height="11" fill="none" stroke="currentColor"/><path d="M2.5 6l2.5 2.5 5-6" fill="none" stroke="currentColor" stroke-width="1.6"/></svg>We’re building America, one Veteran career at a time</li>
    </ul>
    <p class="web-address">www.bdrtexas.com</p>
  </section>

  <section class="panel panel--service">
    <h2 class="panel-title panel-title--dark">Community Service</h2>
    <h3 class="subhead">Disaster Response</h3>
    <ul class="checklist checklist--service">
      <li><svg class="check" viewBox="0 0 12 12"><rect x=".5" y=".5" width="11" height="11" fill="none" stroke="currentColor"/><path d="M2.5 6l2.5 2.5 5-6" fill="none" stroke="currentColor" stroke-width="1.6"/></svg>
        <p class="event-title"><b>Louisiana Flooding</b> - Sept 2016</p>
        <p class="body-copy">As the 15th anniversery of 9/11 approached BDR worked to find a volunteer opportunity. An ambitious plan was formed to respond to the devastating 1000-year flood event in Baton Rouge. With little time for planning, BDR organized all the tools and supplies necessary to take 24 Veterans to assist a community in extreme poverty. The team gutted the homes of nine residents which included: single mothers, handicapped elderaly and a Korean War Veterans</p>
      </li>
      <li><svg class="check" viewBox="0 0 12 12"><rect x=".5" y=".5" width="11" height="11" fill="none" stroke="currentColor"/><path d="M2.5 6l2.5 2.5 5-6" fill="none" stroke="currentColor" stroke-width="1.6"/></svg>
        <p class="event-title"><b>Hurricane Orlend</b> - Oct 2016</p>
        <p class="body-copy">In a period of 24 hours BDR mobilized 16 Veterans with the supplies neccessary to be 100% self-reliant. The team arrived in Holly Hill, SC 8 hours after Hurrican Orlend made landfall. During a period of 2 days, BDR provided over 5,000 meals, distributed 40,000 bottles of water and removed nearly 100 trees.</p>
      </li>
    </ul>
    <p class="web-address">www.bdrtexas.com</p>
  </section>
</main>
</body>
</html>
```